依頼詳細
タワーマンションの理事長にチラシを配布しようと思っています。そのチラシデザイン制作をお願いします。見る人が思わず参加したくなるようなインパクトのあるデザインをお願いします。
記載項目
社名:株式会社MN建築設計/電話:06-4827-3956/URL:http://mn-kenchiku.co.jp
サイズ
A4
ページ数
両面
希望イメージ
シンプル 複雑
単色 カラフル
暗い 明るい
日常 高級
遊び心 厳粛
未来的 伝統的
女性的 男性的

弊社のイメージカラーに合っていたこと、内容が見やすくて分かりやすかった為

このたびは短い期間でありながらもご参加いただきありがとうございました。
皆様の提案は全て良かったので選定に苦慮いたしました。今回選定されなかったご提案者様は残念な結果となりましたが、今後もご提案をお願いするときには是非参加くださいますようお願い申し上げます。

```html
<!DOCTYPE html>
<html lang="ja">
<head>
<meta charset="utf-8">
<title>タワーマンション管理組合 交流会</title>
<link href="https://fonts.googleapis.com/css2?family=Noto+Sans+JP:wght@400;500;700;900&display=swap" rel="stylesheet">
<style>
:root{
  --navy:#16307a;
  --blue:#1f57c3;
  --sky-top:#3f86d8;
  --sky-bottom:#bfe0f7;
  --yellow:#ffe100;
  --red:#e3142d;
  --white:#ffffff;
  --ink:#1a1a1a;
  --pale:#eef5fc;
}
*{margin:0;padding:0;box-sizing:border-box}
html,body{width:849px;height:1200px;overflow:hidden;background:var(--white)}
body{font-family:"Noto Sans JP",sans-serif;color:var(--ink)}
.flyer{position:relative;width:849px;height:1200px;overflow:hidden}
.hero{position:absolute;left:0;top:0;width:849px;height:806px;
  background:linear-gradient(180deg,var(--sky-top) 0%,#79b5ea 45%,var(--sky-bottom) 100%)}
.tower-photo{position:absolute;left:170px;top:400px;width:500px;height:406px;
  background:linear-gradient(180deg,#d9dde3 0%,#9ea9b6 60%,#7c8898 100%);
  clip-path:polygon(18% 0,82% 0,88% 100%,12% 100%)}
.organizer{position:absolute;left:50%;top:30px;transform:translateX(-50%);
  background:var(--blue);color:var(--white);font-size:17px;font-weight:500;
  padding:4px 26px;border-radius:16px;white-space:nowrap}
.title-sub{position:absolute;left:0;width:849px;top:76px;text-align:center;
  font-size:40px;font-weight:900;color:var(--navy);letter-spacing:1px}
.title-main{position:absolute;left:0;width:849px;top:150px;text-align:center;
  font-size:118px;font-weight:900;color:var(--yellow);letter-spacing:6px;
  -webkit-text-stroke:5px var(--navy);paint-order:stroke fill}
.tagline{position:absolute;left:0;width:849px;top:300px;text-align:center;
  font-size:34px;font-weight:900;color:var(--white);
  -webkit-text-stroke:6px var(--navy);paint-order:stroke fill}
.bubble{position:absolute;width:112px;height:112px;border-radius:50%;
  background:var(--white);border:3px solid var(--blue);
  display:flex;align-items:center;justify-content:center;text-align:center;
  font-size:16px;font-weight:700;color:var(--navy);line-height:1.3}
.bubble::after{content:"";position:absolute;left:50%;bottom:-12px;margin-left:-8px;
  border:8px solid transparent;border-top:12px solid var(--blue);border-bottom:0}
.person{position:absolute;width:66px;height:66px;border-radius:50%;
  background:linear-gradient(180deg,#f3d2b3,#3a62b8)}
.capacity{position:absolute;left:680px;top:610px;width:146px;height:146px;border-radius:50%;
  background:var(--yellow);border:4px solid var(--navy);
  display:flex;flex-direction:column;align-items:center;justify-content:center;
  color:var(--navy);font-weight:900;line-height:1}
.capacity .pre{font-size:26px}
.capacity .num{font-size:58px}
.capacity .suf{font-size:26px}
.info{position:absolute;left:0;top:806px;width:849px;height:312px;background:var(--blue)}
.label{display:inline-block;background:var(--navy);color:var(--white);font-weight:700;
  font-size:26px;padding:2px 14px}
.when{position:absolute;left:28px;top:20px;color:var(--white)}
.date{position:absolute;left:28px;top:62px;color:var(--yellow);font-weight:900;font-size:30px;white-space:nowrap}
.date .big{font-size:58px}
.date .dow{display:inline-block;background:var(--red);color:var(--white);font-size:28px;
  padding:0 6px;margin-left:4px;vertical-align:12px}
.time{position:absolute;left:140px;top:138px;color:var(--white);font-size:30px;font-weight:700}
.where{position:absolute;left:28px;top:182px}
.venue{position:absolute;left:28px;top:224px;color:var(--white);font-size:24px;font-weight:700}
.deadline{position:absolute;left:20px;top:262px;background:var(--red);color:var(--white);
  font-size:22px;font-weight:900;padding:3px 12px;white-space:nowrap}
.deadline small{font-size:18px}
.program{position:absolute;left:425px;top:16px;width:404px;height:246px;background:var(--pale);
  padding:14px 18px;color:var(--navy)}
.session{margin-bottom:14px}
.session .slot{font-size:22px;font-weight:900}
.session .name{font-size:20px;font-weight:900;color:var(--red)}
.session .name em{font-style:normal;font-size:14px;color:var(--navy)}
.session .note{font-size:13px;line-height:1.45;color:var(--ink)}
.session .lecturer{font-size:18px;font-weight:700}
.session .lecturer small{font-size:13px}
.safety{position:absolute;left:0;top:1118px;width:849px;height:82px;background:var(--white);padding:10px 28px}
.safety h2{font-size:17px;font-weight:900;color:var(--blue)}
.safety p{font-size:12px;line-height:1.5;width:600px}
.icons{position:absolute;right:28px;top:22px;display:flex;gap:10px}
.icons svg{width:42px;height:42px}
</style>
</head>
<body>
<div class="flyer">
  <section class="hero">
    <div class="tower-photo" role="img" aria-label="青空を背景に建つタワーマンションの写真"></div>
    <div class="organizer">主催：マンション管理組合交流会</div>
    <h1 class="title-sub">タワーマンション管理組合</h1>
    <div class="title-main">交流会</div>
    <p class="tagline">管理組合の自立を目指す！</p>

    <div class="bubble" style="left:42px;top:82px">管理費の<br>値上げ？</div>
    <div class="person" role="img" aria-label="悩む住民のイラスト" style="left:65px;top:206px"></div>

    <div class="bubble" style="left:42px;top:290px">他の<br>タワー<br>マンション<br>はどう？</div>
    <div class="person" role="img" aria-label="考える住民のイラスト" style="left:65px;top:414px"></div>

    <div class="bubble" style="left:242px;top:400px">理事の<br>なり手が<br>いないが<br>どうする？</div>
    <div class="person" role="img" aria-label="困った表情の理事のイラスト" style="left:265px;top:524px"></div>

    <div class="bubble" style="left:462px;top:400px">民泊問題<br>はどうする？</div>
    <div class="person" role="img" aria-label="疑問を持つ住民のイラスト" style="left:485px;top:524px"></div>

    <div class="bubble" style="left:695px;top:82px">分譲<br>マンション<br>の未来を<br>考える</div>
    <div class="person" role="img" aria-label="未来を考える住民のイラスト" style="left:718px;top:206px"></div>

    <div class="bubble" style="left:695px;top:290px">修繕費<br>が高く<br>ない？</div>
    <div class="person" role="img" aria-label="費用を心配する住民のイラスト" style="left:718px;top:414px"></div>

    <div class="capacity"><span class="pre">先着</span><span class="num">15</span><span class="suf">名様</span></div>
  </section>

  <section class="info">
    <div class="when"><span class="label">日時</span></div>
    <div class="date">2022年 <span class="big">7</span>月<span class="big">31</span>日<span class="dow">日</span></div>
    <div class="time">10:00～12:00</div>
    <div class="where"><span class="label">会場</span></div>
    <div class="venue">スカイタワー堺筋本町</div>
    <div class="deadline">申込締切 <small>2022年</small>7月19日<small>(火)</small></div>

    <div class="program">
      <div class="session">
        <div class="slot">10:00～10:50</div>
        <div class="name">第1部 意見交流会 <em>（全員参加型）</em></div>
        <p class="note">各マンションの課題や取り組みを共有し、<br>参加者同士で自由に意見交換を行います。</p>
      </div>
      <div class="session">
        <div class="slot">10:50～11:50</div>
        <div class="name">第2部 修繕工事の進め方と考え方</div>
        <div class="lecturer">講師：三浦 健 <small>（一級建築士）</small></div>
      </div>
    </div>
  </section>

  <footer class="safety">
    <h2>新型コロナウィルス対策について</h2>
    <p>会場では手指の消毒とマスクの着用にご協力ください。発熱や体調不良のある方はご参加をお控えいただき、換気と座席の間隔確保を行います。</p>
    <div class="icons">
      <svg viewBox="0 0 42 42"><circle cx="21" cy="21" r="20" fill="#1f57c3"/><rect x="11" y="16" width="20" height="11" rx="4" fill="#fff"/></svg>
      <svg viewBox="0 0 42 42"><circle cx="21" cy="21" r="20" fill="#1f57c3"/><rect x="16" y="14" width="10" height="17" rx="2" fill="#fff"/><rect x="19" y="9" width="4" height="5" fill="#fff"/></svg>
      <svg viewBox="0 0 42 42"><circle cx="21" cy="21" r="20" fill="#1f57c3"/><path d="M10 21h22M26 15l6 6-6 6M16 15l-6 6 6 6" stroke="#fff" stroke-width="3" fill="none"/></svg>
    </div>
  </footer>
</div>
</body>
</html>
```